Packaging Design for Vanta Core

We require an outstanding packaging design for our Vanta Core brand, which offers hydration electrolyte supplements specifically tailored for athletes and sporty individuals.

Benchmark packaging design from liquora competitor attached. The product packaging contains 20 x 20g sticks of the product.

Target Market

Psychographic: Health-conscious, active lifestyle, values quality, functionality and sustainability.

product description 1:
HYDRATION BOOSTER
Refresh, Replenish, Recharge!

product description 2:
PREMIUM ISOTONIC ELECTROLYTE DRINK
Nutritional Expertise Since 1992.

Existing Logo: to add "since 1992"

Appeal to Target Market: Create a design that resonates with both men and women in the 25-55 age group.

Grafik Design: Develop a visually striking design that grabs attention in online retail environments like Brindle.

Visuals: glass of water (or symbolic) and sticks (powder) just like benchmark brand liquora.

Design Elements
Use colours that are inside the Vanta-Core Logo, attached.
Product will be available in 3 flavours. Lemon=yellow, Orange=orange, Black Currant=purple

Typography: Utilize strong, clean, and modern fonts. Ensure readability and create a sense of strength, endurance and reliability.

The product will be available in 3 flavours: Lemon, Orange and Johannisbeere

We look forward to seeing your creative ideas and innovative designs for our Vanta Core brand packaging.

```html
<!DOCTYPE html>
<html lang="en">
<head>
<meta charset="utf-8">
<title>Vanta Core Hydration Booster – Orange</title>
<link rel="stylesheet" href="https://fonts.googleapis.com/css2?family=Montserrat:wght@300;400;500;600;800&display=swap">
<style>
  :root{
    --bg:#cbcbcb;
    --blue:#2433a6;
    --blue-deep:#1c2a95;
    --yellow:#f7c21d;
    --amber:#f9a92a;
    --orange:#f47b20;
    --orange-deep:#e8531a;
    --brand-yellow:#e4e21c;
    --white:#ffffff;
  }
  *{box-sizing:border-box;margin:0;padding:0}
  html,body{width:1200px;height:800px;overflow:hidden}
  body{background:var(--bg);font-family:"Montserrat",sans-serif;position:relative;color:var(--white)}

  .pouch{position:absolute;left:170px;top:90px;width:540px;height:620px;border-radius:6px;overflow:hidden;
    background:linear-gradient(180deg,var(--orange) 0%,var(--orange-deep) 100%)}
  .pouch__top{position:absolute;left:0;top:0;width:100%;height:255px;background:linear-gradient(180deg,var(--blue-deep),var(--blue))}
  .pouch__bands{position:absolute;left:0;top:255px;width:100%;height:60px}
  .pouch__bands span{display:block;height:15px}
  .pouch__bands span:nth-child(1){background:var(--yellow)}
  .pouch__bands span:nth-child(2){background:var(--amber)}
  .pouch__bands span:nth-child(3){background:#fb9a2a}
  .pouch__bands span:nth-child(4){background:#f78a24}

  .count-tag{position:absolute;left:50px;top:0;width:76px;height:170px;background:var(--orange);
    clip-path:polygon(0 0,100% 0,100% 100%,50% 93%,0 100%);text-align:center;padding-top:100px}
  .count-tag__box{display:inline-flex;align-items:center;gap:2px;border:1px solid var(--blue);border-radius:3px;padding:1px 3px}
  .count-tag__num{font-weight:800;font-size:20px;color:var(--blue);line-height:1}
  .count-tag__label{font-size:8px;line-height:1;text-align:left;color:var(--white)}
  .count-tag__sub{font-size:7px;margin-top:4px}

  .brand{position:absolute;left:0;width:100%;top:130px;text-align:center}
  .brand__name{display:inline-flex;align-items:center;gap:10px;font-weight:800;font-size:40px;color:var(--brand-yellow);letter-spacing:-0.5px}
  .brand__dot{width:24px;height:24px;border-radius:50%;background:#e0327e}
  .brand__since{font-size:12px;color:var(--brand-yellow);margin-top:4px}

  .headline{position:absolute;left:55px;top:350px}
  .headline__main{font-weight:800;font-size:38px;line-height:1}
  .headline__sub{font-weight:400;font-size:38px;line-height:1.05}
  .headline__tag{font-weight:500;font-size:11px;margin-top:6px;margin-left:4px}

  .benefits{position:absolute;left:55px;top:505px;display:flex;align-items:flex-end}
  .benefit{display:flex;flex-direction:column;align-items:center;gap:6px;font-size:13px;font-weight:500;padding:0 12px;border-left:1px solid rgba(255,255,255,.7)}
  .benefit:first-child{border-left:none;padding-left:0}
  .benefit svg{width:24px;height:24px;fill:none;stroke:var(--white);stroke-width:1.4}

  .footer-note{position:absolute;left:120px;top:575px;width:240px;text-align:center;font-size:9px;font-weight:500;line-height:1.5}

  .serve-visual{position:absolute;left:330px;top:235px;width:150px;height:345px;border-radius:8px;
    background:linear-gradient(180deg,rgba(244,160,110,.85),rgba(232,110,60,.9) 60%,#f5a623 100%)}
  .flavour{position:absolute;left:488px;top:500px;transform:rotate(-90deg);transform-origin:left top;font-weight:800;font-size:20px;letter-spacing:1px}

  .stick{position:absolute;left:890px;top:130px;width:130px;height:560px;overflow:hidden;border-radius:3px;transform:rotate(-14deg)}
  .stick__face{position:absolute;left:-215px;top:215px;width:560px;height:130px;transform:rotate(-90deg);display:flex;
    background:linear-gradient(180deg,var(--amber),var(--orange) 40%,var(--orange-deep))}
  .stick__body{flex:1;display:flex;align-items:center;gap:14px;padding-left:16px}
  .stick__weight{font-weight:600;font-size:12px;transform:rotate(90deg)}
  .stick__notes{font-size:7px;line-height:1.4;text-align:center}
  .stick__benefits{font-size:10px;line-height:1.7;border-left:1px solid rgba(255,255,255,.7);padding-left:6px}
  .stick__title{display:flex;flex-direction:column}
  .stick__title b{font-weight:800;font-size:23px;line-height:1}
  .stick__title span{font-size:23px;line-height:1.05;font-weight:400}
  .stick__title small{font-size:7px;font-weight:500}
  .stick__flav{margin-top:4px;align-self:flex-start;background:var(--white);color:var(--orange);font-weight:800;font-size:10px;border-radius:8px;padding:1px 6px}
  .stick__brand{width:190px;background:var(--blue);display:flex;align-items:center;justify-content:center;gap:6px}
  .stick__brand-name{font-weight:800;font-size:22px;color:var(--brand-yellow)}
  .stick__brand .brand__dot{width:14px;height:14px}
</style>
</head>
<body>
  <section class="pouch">
    <div class="pouch__top"></div>
    <div class="pouch__bands"><span></span><span></span><span></span><span></span></div>

    <div class="count-tag">
      <div class="count-tag__box"><span class="count-tag__num">20</span><span class="count-tag__label">Stick<br>Packs</span></div>
      <div class="count-tag__sub">20 Sticks 12.9g</div>
    </div>

    <div class="brand">
      <div class="brand__name"><span class="brand__dot"></span>Vanta Core</div>
      <div class="brand__since">since 1992</div>
    </div>

    <div class="serve-visual" role="img" aria-label="Stick pack pouring orange powder into a glass of water with an orange slice"></div>

    <div class="headline">
      <div class="headline__main">HYDRATION</div>
      <div class="headline__sub">BOOSTER</div>
      <div class="headline__tag">Premium Isotonic Electrolyte Drink</div>
    </div>

    <div class="benefits">
      <div class="benefit">
        <svg viewBox="0 0 24 24"><circle cx="12" cy="12" r="9"/><path d="M12 8v8M8 12h8"/></svg>Refresh
      </div>
      <div class="benefit">
        <svg viewBox="0 0 24 24"><path d="M5 4c-2 3-2 5 0 5s2-2 0-5zM12 4c-2 3-2 5 0 5s2-2 0-5zM19 4c-2 3-2 5 0 5s2-2 0-5z"/><path d="M3 14q3-2 6 0t6 0 6 0M3 18q3-2 6 0t6 0 6 0"/></svg>Replenish
      </div>
      <div class="benefit">
        <svg viewBox="0 0 24 24"><rect x="7" y="4" width="10" height="18" rx="1"/><path d="M10 2h4M13 8l-3 5h4l-3 5"/></svg>Recharge
      </div>
    </div>

    <div class="flavour">ORANGE</div>

    <div class="footer-note">Nutritional Expertise Since 1992.<br>DIETARY SUPLEMENT</div>
  </section>

  <section class="stick">
    <div class="stick__face">
      <div class="stick__body">
        <div class="stick__weight">12.9g</div>
        <div class="stick__notes">Nutritional Expertise<br>Since 1992.<br>DIETARY SUPLEMENT</div>
        <div class="stick__benefits">Refresh<br>Replenish<br>Recharge</div>
        <div class="stick__title">
          <b>HYDRATION</b>
          <span>BOOSTER</span>
          <small>Premium Isotonic Electrolyte Drink</small>
          <em class="stick__flav">ORANGE</em>
        </div>
      </div>
      <div class="stick__brand"><span class="brand__dot"></span><span class="stick__brand-name">Vanta Core</span></div>
    </div>
  </section>
</body>
</html>
```